Tending Our Garden eBook Cover Design

I want to deisgn a cover for my eBook (FRONT COVER) and the title is:

What I Grew From a Single Spark. And Why It Matters
By KT Dorran

TITLE CHANGED TO: UNDER THE WILLOW TREE; WHERE I FOUND MY QUIET STRENGTH AND WHERE YOU MIGHT TOO

The color palette is attached. Along with some photos options of me. Along with the ebook in WORD Document. My website is www.KTDorranLive.example. You can use a different color palette if you think it is best

Target Market(s)

women who look to build a personal brand

Industry/Entity Type

health and wellness

Requirements
Must have
• the title
Nice to have
• use my picture on the cover; but that is optional
Should not have
• any men

```html
<!DOCTYPE html>
<html lang="en">
<head>
<meta charset="utf-8">
<title>Under the Willow Tree — KT Dorran</title>
<link rel="stylesheet" href="https://fonts.googleapis.com/css2?family=Anton&family=Roboto:wght@900&display=swap">
<style>
  :root {
    --cover-blue: #1565c0;
    --title-white: #ffffff;
    --ink-black: #000000;
    --author-ink: #1a0a0c;
    --accent-gold: #fdb62f;
    --city-light: #b2c4c2;
    --city-mid: #8fa9a4;
    --city-deep: #56847f;
    --water-blue: #2a72c4;
  }
  html, body {
    margin: 0;
    padding: 0;
    width: 800px;
    height: 1200px;
    overflow: hidden;
    background: var(--cover-blue);
  }
  .cover {
    position: relative;
    width: 800px;
    height: 1200px;
    background: var(--cover-blue);
  }
  .cover-art {
    position: absolute;
    inset: 0;
    width: 800px;
    height: 1200px;
    display: block;
  }
  .title-line {
    font-family: "Anton", "Oswald", sans-serif;
    fill: var(--title-white);
  }
  .subtitle-band { fill: var(--title-white); }
  .subtitle-text {
    font-family: "Anton", "Oswald", sans-serif;
    fill: var(--ink-black);
  }
  .growth-line {
    fill: none;
    stroke: var(--accent-gold);
    stroke-width: 9;
    stroke-linejoin: miter;
  }
  .value-mark {
    font-family: "Anton", "Oswald", sans-serif;
    fill: var(--title-white);
  }
  .author-band { fill: var(--accent-gold); }
  .author-name {
    font-family: "Roboto", "Arial", sans-serif;
    font-weight: 900;
    fill: var(--author-ink);
    letter-spacing: 4px;
  }
</style>
</head>
<body>
<main class="cover">
  <svg class="cover-art" viewBox="0 0 800 1200" xmlns="http://www.w3.org/2000/svg">
    <defs>
      <linearGradient id="skylineTone" x1="0" y1="0" x2="0" y2="1">
        <stop offset="0" stop-color="var(--city-light)" stop-opacity="0"/>
        <stop offset="0.25" stop-color="var(--city-light)"/>
        <stop offset="0.6" stop-color="var(--city-mid)"/>
        <stop offset="1" stop-color="var(--city-deep)"/>
      </linearGradient>
      <linearGradient id="waterTone" x1="0" y1="0" x2="0" y2="1">
        <stop offset="0" stop-color="var(--water-blue)"/>
        <stop offset="1" stop-color="var(--cover-blue)"/>
      </linearGradient>
    </defs>

    <g class="title-block">
      <text class="title-line" x="69" y="205" font-size="158" textLength="664" lengthAdjust="spacingAndGlyphs">UNDER THE</text>
      <text class="title-line" x="67" y="300" font-size="95" textLength="662" lengthAdjust="spacingAndGlyphs">WILLOW TREE;</text>
      <text class="title-line" x="67" y="395" font-size="95" textLength="662" lengthAdjust="spacingAndGlyphs">WHERE I FOUND MY QUIET</text>
      <text class="title-line" x="73" y="650" font-size="270" textLength="651" lengthAdjust="spacingAndGlyphs">STRENGTH</text>
    </g>

    <g class="subtitle">
      <rect class="subtitle-band" x="71" y="679" width="658" height="108"/>
      <text class="subtitle-text" x="84" y="767" font-size="92" textLength="632" lengthAdjust="spacingAndGlyphs">AND WHERE YOU MIGHT TOO</text>
    </g>

    <g class="city-scene" role="img" aria-label="City skyline silhouette in grey-green tones with its reflection on water">
      <rect x="0" y="800" width="800" height="256" fill="url(#skylineTone)"/>
      <rect x="0" y="1056" width="800" height="134" fill="url(#waterTone)"/>
    </g>

    <g class="growth-chart">
      <polyline class="growth-line" points="76,1050 182,963 274,1046 427,911 509,987 727,810"/>
      <text class="value-mark" x="400" y="1006" font-size="230" text-anchor="middle">$</text>
    </g>

    <g class="author">
      <rect class="author-band" x="175" y="1087" width="449" height="74"/>
      <text class="author-name" x="400" y="1145" font-size="58" text-anchor="middle">KT DORRAN</text>
    </g>
  </svg>
</main>
</body>
</html>
```